prestige web design for KELVA Finance

Hi Guys,

Looking to team up with a creative designer for another of our websites for KELVA finance.
if looking for our similar website www.brimlendco.com.au is one of our other companies. ideally working in our logo being black and white.

Please see attachments for our logo and a description
HOME
VEHICLE
EQUIPMENT
WHO WE ARE
CONTACT US

open to ideas on layout .

touch base if you have any questions.

Target Market(s)

Prestige cars and equipment -trucks earthmoving

Industry/Entity Type

finance

Coding

Coded - Design and coding required

Number of Pages Required

5+ page

Font styles to use
Sans Serif

Colors

Designer to choose colors to be used in the design.

```html
<!DOCTYPE html>
<html lang="en">
<head>
<meta charset="utf-8">
<title>KELVA Finance</title>
<link rel="stylesheet" href="https://fonts.googleapis.com/css2?family=Montserrat:wght@300;400;500;600;700&family=Poppins:wght@300;400;500;600;700;800&display=swap">
<style>
:root{
  --ink:#111111;
  --black:#000000;
  --white:#ffffff;
  --panel:#222222;
  --mist:#ececec;
  --line:#8a8a8a;
  --muted:#7d7d7d;
  --field:#b9b9b9;
}
*{margin:0;padding:0;box-sizing:border-box}
html,body{width:1200px;height:3664px;overflow:hidden}
body{position:relative;background:var(--white);font-family:"Montserrat",sans-serif;color:var(--ink)}
.abs{position:absolute}
.brand{font-family:"Poppins",sans-serif;font-weight:600;color:var(--white);letter-spacing:1px;white-space:nowrap}

/* hero */
.hero{left:0;top:0;width:1200px;height:704px;background:linear-gradient(100deg,#3a2a1b 0%,#6b4a2a 35%,#9b7a55 62%,#c9a070 80%,#7a5a3a 100%)}
.hero-vehicle{left:440px;top:180px;width:720px;height:420px;background:radial-gradient(ellipse at 50% 55%,#d8dadd 0%,#9ea3a8 45%,rgba(80,80,80,0) 72%)}
.nav{left:0;top:0;width:960px;height:70px;font-size:13px;color:#d6d6d6}
.nav a,.nav .sep{position:absolute;top:28px;color:#d6d6d6;text-decoration:none;letter-spacing:.2px;white-space:nowrap;line-height:16px}
.nav a.active{color:var(--white);font-weight:600}
.call{left:971px;top:14px;width:171px;height:39px;border-radius:20px;background:var(--white);display:flex;align-items:center;justify-content:center;gap:6px;font-weight:700;font-size:14px;color:var(--black);white-space:nowrap}
.kicker-rule{left:0;top:277px;width:100px;height:1px;background:var(--white)}
.kicker{left:116px;top:264px;font-size:22px;letter-spacing:4px;color:var(--white);font-weight:400}
.headline{left:115px;top:290px;font-family:"Poppins",sans-serif;font-weight:800;font-size:70px;line-height:70px;color:var(--white)}
.scroll{left:560px;top:558px;width:118px;text-align:center;font-size:12px;letter-spacing:3px;color:var(--white);font-weight:600}

/* calculator */
.grey-block{left:0;top:704px;width:609px;height:573px;background:var(--mist)}
.calc{left:97px;top:640px;width:1019px;height:253px;background:var(--white);box-shadow:0 2px 8px rgba(0,0,0,.08)}
.calc h2{position:absolute;left:49px;top:30px;font-family:"Poppins",sans-serif;font-weight:500;font-size:23px;color:#222}
.field{position:absolute;width:285px;border-bottom:1.5px solid var(--line)}
.field label{display:block;font-size:12px;color:var(--muted);margin-bottom:6px}
.field span{display:block;font-size:17px;color:#222;padding-bottom:9px}
.calc-btn{position:absolute;left:699px;top:158px;width:285px;height:45px;background:var(--black);color:var(--white);font-weight:700;font-size:14px;letter-spacing:1px;display:flex;align-items:center;justify-content:center;gap:8px}

/* who we are */
.interior{left:97px;top:957px;width:621px;height:474px;background:linear-gradient(135deg,#1b1613 0%,#4a2f25 40%,#6b4536 60%,#2a211d 100%)}
.who{left:647px;top:1032px;width:481px;height:322px;background:var(--panel);color:var(--white);text-align:center}
.who h2{margin-top:58px;font-family:"Poppins",sans-serif;font-weight:300;font-size:34px}
.who h2 b,.sec-title b{font-weight:700}
.who p{margin:18px auto 0;width:360px;font-size:15px;line-height:25px}
.outline-btn{display:inline-block;margin-top:22px;width:161px;height:47px;line-height:44px;border:2px solid var(--white);border-radius:24px;font-size:13px;font-weight:700;letter-spacing:1px}

/* equipment */
.sec-title{font-family:"Poppins",sans-serif;font-weight:300;font-size:34px;white-space:nowrap}
.equip-photo{left:607px;top:1544px;width:593px;height:458px;background:linear-gradient(180deg,#9fb1c4 0%,#d9dde0 38%,#c9a13a 55%,#b8905a 75%,#8d7458 100%)}
.equip-copy{left:100px;top:1675px;width:460px;text-align:center}
.equip-copy p{margin:18px auto 0;width:440px;font-size:15.5px;line-height:28px;color:#333}
.pill{display:inline-block;width:158px;height:46px;line-height:46px;border-radius:23px;font-size:13px;font-weight:700;letter-spacing:1px;text-align:center}
.pill.dark{background:var(--black);color:var(--white)}
.pill.light{background:var(--white);color:var(--black)}

/* vehicle */
.vehicle{left:0;top:2002px;width:1200px;height:565px;background:linear-gradient(180deg,#4a3a35 0%,#8a6a5a 25%,#3b2c27 55%,#2a201c 100%)}
.vehicle-car{left:120px;top:2120px;width:500px;height:300px;background:radial-gradient(ellipse at 50% 50%,#c9c6bf 0%,#8b867d 45%,rgba(60,50,45,0) 72%)}
.vehicle-copy{left:585px;top:2165px;width:500px;text-align:center;color:var(--white)}
.vehicle-copy p{margin-top:14px;font-size:18px;line-height:29px}
.vline{left:600px;top:2531px;width:3px;height:78px;background:var(--black)}

/* contact */
.contact{left:0;top:2567px;width:1200px;height:593px;background:linear-gradient(180deg,#fafafa 0%,#eeeeee 60%,#e2e2e2 100%)}
.contact-head{left:240px;top:2680px;width:712px;text-align:center}
.contact-head p{margin-top:18px;font-size:18px;line-height:30px;color:#333}
.footer{left:0;top:3160px;width:1200px;height:504px;background:var(--black)}
.form{left:223px;top:2875px;width:754px;height:393px;background:var(--white)}
.input{position:absolute;height:47px;border:1.5px solid var(--field);border-radius:24px;padding-left:30px;line-height:44px;font-size:14px;color:#333}
.textarea{position:absolute;left:50px;top:174px;width:653px;height:111px;border:1.5px solid var(--field);border-radius:14px;padding:20px 22px;font-size:14px;color:#333}
.send{position:absolute;left:293px;top:296px;width:169px;height:41px;line-height:41px;border-radius:21px;background:var(--black);color:var(--white);text-align:center;font-size:13px;font-weight:700;letter-spacing:1px}

/* footer */
.social{position:absolute;top:3431px;width:27px;height:27px;border-radius:50%;background:var(--white)}
.col-rule{position:absolute;top:3270px;width:1px;height:260px;background:#2e2e2e}
.col-head{position:absolute;top:3350px;padding-left:12px;border-left:2px solid var(--white);font-size:16px;font-weight:500;color:var(--white);line-height:20px}
.col-links{position:absolute;top:3385px;list-style:none;font-size:13px;color:#d0d0d0;line-height:27px}
.contact-item{position:absolute;left:887px;display:flex;align-items:center;gap:12px;color:var(--white);font-size:13px;line-height:19px}
.contact-item strong{font-weight:700;display:block}
.bottom-rule{left:0;top:3590px;width:1200px;height:1px;background:#333}
.copyright{left:0;top:3612px;width:1200px;text-align:center;font-size:13px;color:#cfcfcf}
</style>
</head>
<body>

<header>
  <div class="abs hero" role="img" aria-label="Photo of a silver luxury SUV parked on a rocky hillside at sunset"></div>
  <div class="abs hero-vehicle" role="img" aria-label="Silver SUV"></div>
  <div class="abs brand" style="left:85px;top:14px;font-size:34px">KELVA Finance</div>
  <nav class="abs nav">
    <a class="active" href="#" style="left:385px">HOME</a><span class="sep" style="left:453px">|</span>
    <a href="#" style="left:477px">VEHICLE</a><span class="sep" style="left:556px">|</span>
    <a href="#" style="left:582px">EQUIPMENT</a><span class="sep" style="left:686px">|</span>
    <a href="#" style="left:712px">WHO WE ARE</a><span class="sep" style="left:823px">|</span>
    <a href="#" style="left:851px">CONTACT US</a>
  </nav>
  <div class="abs call">
    <svg width="15" height="15" viewBox="0 0 24 24"><path fill="#000" d="M6.6 10.8a15 15 0 0 0 6.6 6.6l2.2-2.2c.3-.3.7-.4 1-.2 1.1.4 2.3.6 3.6.6.6 0 1 .4 1 1V20c0 .6-.4 1-1 1A17 17 0 0 1 3 4c0-.6.4-1 1-1h3.5c.6 0 1 .4 1 1 0 1.3.2 2.5.6 3.6.1.3 0 .7-.2 1z"/></svg>
    1300 418 2275
  </div>
  <div class="abs kicker-rule"></div>
  <div class="abs kicker">KELVA FINANCE</div>
  <h1 class="abs headline">MAKERS OF<br>POSSIBLE</h1>
  <div class="abs scroll">SCROLL
    <svg style="display:block;margin:6px auto 0" width="30" height="18" viewBox="0 0 30 18"><path d="M3 3l12 11L27 3" fill="none" stroke="#fff" stroke-width="4"/></svg>
  </div>
</header>

<section>
  <div class="abs grey-block"></div>
  <div class="abs calc">
    <h2>FINANCE REPAYMENT CALCULATOR</h2>
    <div class="field" style="left:48px;top:89px"><label>Purchase amount</label><span>$100000</span></div>
    <div class="field" style="left:355px;top:89px"><label>Deposit</label><span>$5000</span></div>
    <div class="field" style="left:698px;top:86px"><label>Balloon Payment</label><span>$2000</span></div>
    <div class="field" style="left:48px;top:156px"><label>Term</label><span>5 Year</span></div>
    <div class="field" style="left:358px;top:159px"><label>Interest rate% pa.</label><span>7.5</span></div>
    <div class="calc-btn">CALCULATE
      <svg width="20" height="12" viewBox="0 0 20 12"><path d="M0 6h18M13 1l5 5-5 5" fill="none" stroke="#fff" stroke-width="1.8"/></svg>
    </div>
  </div>
</section>

<section>
  <div class="abs interior" role="img" aria-label="Photo of a luxury car interior with brown leather seats"></div>
  <div class="abs who">
    <h2>WHO <b>WE ARE</b></h2>
    <p>Well, because we're here to help you! We care about outcomes AND helping you achieve a stress and enjoyable lending experience.</p>
    <span class="outline-btn">LEARN MORE</span>
  </div>
  <svg class="abs" style="left:1015px;top:1248px" width="130" height="130" viewBox="0 0 130 130">
    <g fill="#222">
      <circle cx="124" cy="5" r="1.6"/><circle cx="124" cy="17" r="1.6"/><circle cx="124" cy="29" r="1.6"/><circle cx="124" cy="41" r="1.6"/><circle cx="124" cy="53" r="1.6"/><circle cx="124" cy="65" r="1.6"/><circle cx="124" cy="77" r="1.6"/><circle cx="124" cy="89" r="1.6"/><circle cx="124" cy="101" r="1.6"/><circle cx="124" cy="113" r="1.6"/><circle cx="124" cy="124" r="1.6"/>
      <circle cx="5" cy="124" r="1.6"/><circle cx="17" cy="124" r="1.6"/><circle cx="29" cy="124" r="1.6"/><circle cx="41" cy="124" r="1.6"/><circle cx="53" cy="124" r="1.6"/><circle cx="65" cy="124" r="1.6"/><circle cx="77" cy="124" r="1.6"/><circle cx="89" cy="124" r="1.6"/><circle cx="101" cy="124" r="1.6"/><circle cx="113" cy="124" r="1.6"/>
      <circle cx="5" cy="112" r="1.6"/><circle cx="17" cy="112" r="1.6"/><circle cx="29" cy="112" r="1.6"/><circle cx="41" cy="112" r="1.6"/><circle cx="53" cy="112" r="1.6"/><circle cx="65" cy="112" r="1.6"/><circle cx="77" cy="112" r="1.6"/><circle cx="89" cy="112" r="1.6"/><circle cx="101" cy="112" r="1.6"/><circle cx="113" cy="112" r="1.6"/>
    </g>
  </svg>
</section>

<section>
  <div class="abs equip-copy">
    <h2 class="sec-title">KELVA <b>EQUIPMENT</b></h2>
    <p>While you focus on getting the right car, we will focus<br>on getting you the right finance.</p>
    <span class="pill dark" style="margin-top:22px">APPLY NOW</span>
  </div>
  <div class="abs equip-photo" role="img" aria-label="Photo of a yellow excavator loading a mining dump truck under a cloudy sky"></div>
</section>

<section>
  <div class="abs vehicle" role="img" aria-label="Photo of a silver sports car driving on a road at dusk"></div>
  <div class="abs vehicle-car" role="img" aria-label="Silver sports car"></div>
  <div class="abs vehicle-copy">
    <h2 class="sec-title">VEHICLE <b>LOAN</b></h2>
    <p>Well, because we're here to help you!<br>We care about outcomes AND helping you achieve a<br>stress and enjoyable lending experience</p>
    <span class="pill light" style="margin-top:28px">APPLY NOW</span>
  </div>
</section>

<section>
  <div class="abs contact" role="img" aria-label="Faint grey photo of a city skyline"></div>
  <div class="abs vline"></div>
  <div class="abs contact-head">
    <h2 class="sec-title">CONTACT <b>KELVA</b></h2>
    <p>To find out how to get KELVA Finance working for you helping with your funding needs. Please call 13 58 21 (13 KELVA) Or Contact us now: Alternatively send us a message with your questions.</p>
  </div>
  <div class="abs footer"></div>
  <form class="abs form">
    <div class="input" style="left:50px;top:56px;width:321px">First Name</div>
    <div class="input" style="left:383px;top:56px;width:320px">Last Name</div>
    <div class="input" style="left:49px;top:115px;width:321px">Phone</div>
    <div class="input" style="left:382px;top:115px;width:321px">E-mail</div>
    <div class="textarea">Message</div>
    <div class="send">SEND MESSAGE</div>
  </form>
</section>

<footer>
  <div class="abs brand" style="left:119px;top:3350px;font-size:34px">KELVA Finance</div>
  <span class="social" style="left:126px"></span>
  <span class="social" style="left:160px"></span>
  <span class="social" style="left:193px"></span>
  <span class="social" style="left:227px"></span>

  <span class="col-rule" style="left:437px"></span>
  <span class="col-rule" style="left:644px"></span>
  <span class="col-rule" style="left:862px"></span>

  <div class="col-head" style="left:450px">QUICK LINKS</div>
  <ul class="col-links" style="left:465px"><li>Home</li><li>Vehicle</li><li>Equipment</li><li>Who we are</li></ul>

  <div class="col-head" style="left:654px">RESOURCES</div>
  <ul class="col-links" style="left:668px"><li>Terms of Use</li><li>Why Choose Us</li><li>Contact us</li></ul>

  <div class="col-head" style="left:875px">CONTACT US</div>
  <div class="contact-item" style="top:3388px">
    <svg width="32" height="32" viewBox="0 0 32 32"><circle cx="16" cy="16" r="16" fill="#fff"/><path fill="#000" transform="translate(7 7) scale(.75)" d="M6.6 10.8a15 15 0 0 0 6.6 6.6l2.2-2.2c.3-.3.7-.4 1-.2 1.1.4 2.3.6 3.6.6.6 0 1 .4 1 1V20c0 .6-.4 1-1 1A17 17 0 0 1 3 4c0-.6.4-1 1-1h3.5c.6 0 1 .4 1 1 0 1.3.2 2.5.6 3.6.1.3 0 .7-.2 1z"/></svg>
    <div>Phone Number<strong>(02) 8123 4470</strong></div>
  </div>
  <div class="contact-item" style="top:3443px">
    <svg width="32" height="32" viewBox="0 0 32 32"><circle cx="16" cy="16" r="16" fill="#fff"/><rect x="8" y="10.5" width="16" height="11" fill="none" stroke="#000" stroke-width="1.8"/><path d="M8 11l8 6 8-6" fill="none" stroke="#000" stroke-width="1.8"/></svg>
    <div>Email address<strong>hello@kelvafinance.com</strong></div>
  </div>

  <div class="abs bottom-rule"></div>
  <div class="abs copyright">© 2022 KELVA Finance | All Right Reserved</div>
</footer>

</body>
</html>
```